Design my dad a new business card because his current one sucks!

I need a business card designed for my fathers home maintenance business. His customers are individuals (single moms, old people etc.) as well as the occasional business. As such it needs to be accessible to both target audiences.

The front of the card should be dark grey on yellow with the logo and contain the following information:
- Warren Dobrinski
- 0487 362 914
- info@harbourlinehandyworks.com.au
- 0487 362 914

- ABN: 87 214 630 592
- 'Fully Insured'

The reverse should be yellow on dark grey and will have the web address:
- harbourlinehandyworks.com.au

And a few key services he offers:
GENERAL REPAIRS
PAINTING/TILING/
PAVING &CONCRETING
PRESSURE WASHING
ON-SITE WELDING
DECKING ADDITIONS & REPAIRS
FENCING
FULL BOND CLEANING

This will be first time the logo has been printed so you will need to come up with the best CMYK approximation of the RGB colours to make sure it is a close as possible.

```html
<!DOCTYPE html>
<html lang="en">
<head>
<meta charset="utf-8">
<title>Harbourline Handyworks – Business Card</title>
<link rel="stylesheet" href="https://fonts.googleapis.com/css2?family=Ubuntu:wght@400;500;700&display=swap">
<style>
  :root {
    --yellow: #efb92c;
    --yellow-light: #f7d77e;
    --charcoal: #2c2b2e;
    --charcoal-light: #55535a;
    --ink: #1f1e21;
    --backdrop: #ecebe8;
  }
  html, body {
    margin: 0;
    padding: 0;
    width: 1200px;
    height: 1000px;
    overflow: hidden;
    background: var(--backdrop);
    font-family: "Ubuntu", sans-serif;
  }
  .canvas { position: relative; width: 1200px; height: 1000px; }

  .card {
    position: absolute;
    width: 647px;
    height: 390px;
    overflow: hidden;
    box-shadow: 0 6px 18px rgba(0,0,0,0.25);
  }

  /* Front */
  .card-front {
    left: 414px; top: 88px;
    background: radial-gradient(ellipse at 45% 30%, var(--yellow-light) 0%, var(--yellow) 70%);
  }
  .card-front .wave { position: absolute; left: 0; top: 0; }
  .brand-name {
    position: absolute;
    left: 0; right: 0; top: 150px;
    text-align: center;
    font-weight: 700;
    font-size: 52px;
    letter-spacing: -0.5px;
    color: var(--ink);
  }

  /* Back */
  .card-back {
    left: 118px; top: 556px;
    background: var(--charcoal);
  }
  .back-top {
    position: absolute; left: 0; top: 0; width: 100%; height: 195px;
    background: radial-gradient(ellipse at 70% 40%, var(--charcoal-light) 0%, var(--charcoal) 65%);
  }
  .holder-name {
    position: absolute; left: 59px; top: 56px;
    font-size: 26px; font-weight: 700; color: var(--yellow);
  }
  .holder-company {
    position: absolute; left: 59px; top: 97px;
    font-size: 12px; color: var(--yellow);
  }
  .services {
    position: absolute; left: 59px; top: 164px;
    font-size: 15px; font-weight: 500; color: var(--yellow); letter-spacing: 0.2px;
  }
  .contact-band {
    position: absolute; left: 0; top: 195px; width: 100%; height: 160px;
    background: radial-gradient(ellipse at 55% 30%, var(--yellow-light) 0%, var(--yellow) 70%);
  }
  .contact-list { list-style: none; margin: 0; padding: 0; position: absolute; left: 46px; top: 16px; }
  .contact-item {
    display: flex; align-items: center; gap: 10px;
    height: 33.5px;
    font-size: 15px; font-weight: 700; color: var(--ink);
  }
  .contact-item svg { width: 24px; height: 24px; flex: none; }
</style>
</head>
<body>
<main class="canvas">

  <section class="card card-front" aria-label="Card front">
    <svg class="wave" width="647" height="390" viewBox="0 0 647 390" aria-hidden="true">
      <path d="M0 307 C 120 285, 220 318, 310 322 C 430 328, 560 300, 647 255 L647 390 L0 390 Z" fill="var(--charcoal)"/>
    </svg>
    <div class="brand-name">Harbourline Handyworks</div>
  </section>

  <section class="card card-back" aria-label="Card back">
    <div class="back-top">
      <div class="holder-name">Warren Dobrinski</div>
      <div class="holder-company">Harbourline Handyworks</div>
      <div class="services">GENERAL REPAIRS | PAINTING | TILING | CONCRETING | FENCING &amp; MORE</div>
    </div>

    <div class="contact-band">
      <ul class="contact-list">
        <li class="contact-item">
          <svg viewBox="0 0 24 24" aria-hidden="true"><path fill="var(--ink)" d="M12 1l2 6 5-4-2 6 6 1-5 3 5 4-6 0 1 6-5-4-1 6-1-6-5 4 1-6-6 0 5-4-5-3 6-1-2-6 5 4z"/></svg>
          ABN: 87 214 630 592
        </li>
        <li class="contact-item">
          <svg viewBox="0 0 24 24" aria-hidden="true"><circle cx="12" cy="12" r="12" fill="var(--ink)"/><rect x="6" y="8" width="12" height="8" fill="none" stroke="var(--yellow)" stroke-width="1.5"/><path d="M6 8l6 5 6-5" fill="none" stroke="var(--yellow)" stroke-width="1.5"/></svg>
          info@harbourlinehandyworks.com.au
        </li>
        <li class="contact-item">
          <svg viewBox="0 0 24 24" aria-hidden="true"><circle cx="12" cy="12" r="12" fill="var(--ink)"/><path d="M6 10c0-2 3-3 6-3s6 1 6 3v1h-3v-1.5h-6V11H6z" fill="var(--yellow)"/><rect x="8" y="12" width="8" height="5" rx="1" fill="var(--yellow)"/></svg>
          0487 362 914
        </li>
        <li class="contact-item">
          <svg viewBox="0 0 24 24" aria-hidden="true"><g fill="none" stroke="var(--ink)" stroke-width="1.6"><circle cx="12" cy="12" r="10"/><ellipse cx="12" cy="12" rx="4.5" ry="10"/><path d="M2 12h20M4 7h16M4 17h16"/></g></svg>
          www.harbourlinehandyworks.com.au
        </li>
      </ul>
    </div>
  </section>

</main>
</body>
</html>
```